Oven Cleaning Business owner needs business card design

Hi there,
Would like for a business card to be designed for myself, the owner of a professional oven cleaning business on the Sunshine Coast.
Would like it to look sleek, and modern-ish. Bit creative is encouraged too.
Include following:
Name/title: Corin ter Haghe, Owner
Phone number: 1300 482 916
Email: info@hearthshinecrew.com.au
Website: www.hearthshinecrew.com.au

```html
<!DOCTYPE html>
<html lang="en">
<head>
<meta charset="utf-8">
<title>Hearthshine Crew – Business Card</title>
<link rel="stylesheet" href="https://fonts.googleapis.com/css2?family=Montserrat:wght@400;500;600&display=swap">
<style>
  :root{
    --stage:#4a4a4a;
    --paper:#ffffff;
    --paper-shade:#f4f4f4;
    --navy:#1c285c;
    --cyan:#29d8dc;
    --ink:#1f1f24;
  }
  *{box-sizing:border-box;margin:0;padding:0}
  html,body{width:1200px;height:1200px;overflow:hidden}
  body{
    background:var(--stage);
    font-family:"Montserrat",Arial,sans-serif;
    display:flex;flex-direction:column;align-items:center;justify-content:center;gap:60px;
  }
  .card{
    position:relative;width:820px;height:500px;border-radius:34px;overflow:hidden;
    box-shadow:0 14px 30px rgba(0,0,0,.35);
  }
  /* front */
  .card--front{background:linear-gradient(180deg,var(--paper) 0%,var(--paper-shade) 100%)}
  .identity{
    position:absolute;left:80px;top:210px;
    border-left:6px solid var(--cyan);padding-left:14px;line-height:1;
  }
  .identity__name{color:var(--cyan);font-size:34px;font-weight:500;text-transform:uppercase;letter-spacing:-.5px}
  .identity__title{color:var(--ink);font-size:26px;font-weight:400;margin-top:2px}
  .contacts{position:absolute;left:100px;top:318px;list-style:none}
  .contacts li{display:flex;align-items:center;gap:16px;font-size:25px;color:var(--ink);height:42px}
  .contacts svg{width:26px;height:26px;flex:none}
  .brand-front{
    position:absolute;right:70px;top:130px;width:300px;
    display:flex;flex-direction:column;align-items:center;gap:18px;
  }
  .brand-dot{width:70px;height:70px;border-radius:50%;background:var(--cyan)}
  .brand-name{font-weight:600;text-align:center;text-transform:uppercase;line-height:1.05}
  .brand-front .brand-name{color:var(--navy);font-size:38px;letter-spacing:3px}
  .band-cyan{position:absolute;left:0;bottom:0;width:61%;height:18px;background:var(--cyan)}
  .band-navy{position:absolute;right:0;bottom:0;width:37.5%;height:48px;background:var(--navy)}
  .band-navy-edge{position:absolute;right:0;bottom:0;width:10px;height:140px;background:var(--navy)}
  /* back */
  .card--back{background:var(--navy);display:flex;flex-direction:column;align-items:center;justify-content:center;gap:30px}
  .card--back .brand-dot{width:110px;height:110px}
  .card--back .brand-name{color:var(--cyan);font-size:58px;letter-spacing:6px}
</style>
</head>
<body>
  <section class="card card--front" aria-label="Card front">
    <div class="identity">
      <p class="identity__name">Corin ter Haghe</p>
      <p class="identity__title">OWNER</p>
    </div>
    <ul class="contacts">
      <li>
        <svg viewBox="0 0 24 24" aria-hidden="true"><path fill="var(--cyan)" d="M6.6 10.8a15 15 0 0 0 6.6 6.6l2.2-2.2c.3-.3.7-.4 1-.2 1.1.4 2.3.6 3.6.6.6 0 1 .4 1 1V20c0 .6-.4 1-1 1A17 17 0 0 1 3 4c0-.6.4-1 1-1h3.5c.6 0 1 .4 1 1 0 1.3.2 2.5.6 3.6.1.3 0 .7-.2 1z"/></svg>
        <span>1300 482 916</span>
      </li>
      <li>
        <svg viewBox="0 0 24 24" aria-hidden="true"><rect x="2" y="5" width="20" height="14" fill="var(--cyan)"/><path d="M2 5l10 8 10-8" fill="none" stroke="#fff" stroke-width="1.6"/></svg>
        <span>info@hearthshinecrew.com.au</span>
      </li>
      <li>
        <svg viewBox="0 0 24 24" aria-hidden="true"><g fill="none" stroke="var(--cyan)" stroke-width="1.8"><circle cx="12" cy="12" r="9.5"/><ellipse cx="12" cy="12" rx="4.2" ry="9.5"/><path d="M2.5 12h19M4 7h16M4 17h16"/></g></svg>
        <span>www.hearthshinecrew.com.au</span>
      </li>
    </ul>
    <div class="brand-front">
      <span class="brand-dot" aria-hidden="true"></span>
      <p class="brand-name">Hearthshine<br>Crew</p>
    </div>
    <div class="band-cyan"></div>
    <div class="band-navy"></div>
    <div class="band-navy-edge"></div>
  </section>

  <section class="card card--back" aria-label="Card back">
    <span class="brand-dot" aria-hidden="true"></span>
    <p class="brand-name">Hearthshine<br>Crew</p>
  </section>
</body>
</html>
```